Web Design for historic veg friendly, organic restaurant

We need a new web site. The Millbrook Cafe is a 40 year old restaurant in Chicago. We've been one of the premier, casual vegetarian restaurants since we opened. 5 years ago, Millbrook Cafe was purchased from the original owners by a local, certified organic farmer. We are nearly 100% from scratch kitchen, 100% certified organic produce, we are governed by a strict sustainable plan and we are very active politically. But you wouldn't know it form our website! We have a desire to build a simple website around some basic principles:
1. We need our current logo prominently displayed (logo attached)
2. We need a "click to call" easily accessible
3. We have an online order link that needs to be easily accessible
4. We need our hours, location, and directions easy to see
4. We need a separate events page (we have a live music and events venue that runs shows 5-7 nights per week.)
5. We would like to have a separate page for pictures, particularly old pictures. It would be fun to have a function for people to post their own shots, but that might make this too complicated. If it were possible, we would of course need to retain the ability to curate posted pictures.
6. This needs to be easily edited by us, so in a platform such as word press or similar
7. We will need this mobile enhanced

Target Market(s)

Neighborhood residents - zip code is 48213

Industry/Entity Type

Restaurant

Coding

Coded - Design and coding required

Number of Pages Required

4 page

Font styles to use
Sans Serif

Requirements
Must have
• Logo, click to call, events page that we can manage, contact us, about us page, menu (we have the online menu through a third party plugin), a page for our market and some nice pictures on our splash page,
• Must be mobile ready and on a platform such as Word Press or some other platform where we can edit on our own
Nice to have
• Page for past employees and historical pictures, be nice to have food pictures or something similar on a scroll, would love to have an ability for others to post pictures that we would "approve"
Should not have
• We don't need anything that spins, moves, flames or other features that detract from gathering information

```html
<!DOCTYPE html>
<html lang="en">
<head>
<meta charset="utf-8">
<title>Millbrook Cafe</title>
<link rel="stylesheet" href="https://fonts.googleapis.com/css2?family=Roboto:wght@300;400;500;700;900&family=Roboto+Condensed:wght@700&family=Great+Vibes&display=swap">
<style>
:root{
  --red:#e8403a;
  --red-dark:#c9302b;
  --yellow:#fbd92b;
  --ink:#1d1d1d;
  --card:#231f20;
  --green:#7fbf92;
  --grey-bg:#efefef;
  --footer:#1b1b1b;
  --white:#ffffff;
  --muted:#9a9a9a;
}
*{box-sizing:border-box;margin:0;padding:0}
html,body{width:1200px;height:3422px;overflow:hidden}
body{font-family:"Roboto",Arial,sans-serif;color:var(--ink);background:var(--white);position:relative}
section,header,footer{position:absolute;left:0;width:1200px}
.abs{position:absolute}
.photo{position:absolute}

/* top bar + nav */
.topbar{top:0;height:46px;background:var(--red);color:var(--white);display:flex;justify-content:flex-end;align-items:center;gap:14px;padding-right:78px;z-index:3}
.topbar .mail{font-size:11px;display:flex;align-items:center;gap:5px}
.topbar .phone{font-size:20px;font-weight:700;display:flex;align-items:center;gap:6px}
.nav{top:46px;height:64px;background:rgba(255,255,255,.86);z-index:3}
.nav a{position:absolute;top:22px;transform:translateX(-50%);font-size:14px;color:#222;text-decoration:none;font-weight:500}
.nav .dot{position:absolute;top:30px;width:4px;height:4px;border-radius:50%;background:#333}

/* hero */
.hero{top:0;height:634px;overflow:hidden}
.hero .photo{inset:0;background:radial-gradient(ellipse at 30% 55%,#b0461f 0%,#7a2a12 35%,transparent 60%),radial-gradient(ellipse at 82% 40%,#c9953f 0%,#8a5a25 35%,transparent 65%),linear-gradient(120deg,#3b1d0f,#6a3a1c 50%,#2d170c)}
.hero .brand{left:0;width:1200px;top:205px;text-align:center;font-family:"Roboto",sans-serif;font-weight:900;font-size:96px;color:var(--yellow);letter-spacing:1px}
.hero .brand-dot{left:360px;top:224px;width:34px;height:34px;border-radius:50%;background:var(--red)}
.hero .rule{left:374px;top:449px;width:452px;height:1px;background:rgba(255,255,255,.45)}
.arrow{position:absolute;width:34px;height:34px;border-radius:50%;border:1.5px solid rgba(255,255,255,.8);display:flex;align-items:center;justify-content:center}
.btn{position:absolute;height:48px;border-radius:24px;display:flex;align-items:center;justify-content:center;gap:10px;font-weight:700;font-size:21px;text-transform:uppercase}
.btn-order{left:374px;top:495px;width:226px;background:var(--yellow);color:#1a1a1a}
.btn-call{left:616px;top:495px;width:228px;background:var(--red);color:var(--white);border:2px solid var(--white)}

/* welcome */
.welcome{top:634px;height:479px;background:var(--red);color:var(--white)}
.welcome .frame{left:164px;top:50px;width:381px;height:381px;background:#111;padding:10px}
.welcome .frame .photo{inset:10px;background:linear-gradient(135deg,#6d8a3c,#c9b07a 35%,#b94a2a 60%,#4f6a2f 85%,#d6c7a0)}
.welcome h2{left:577px;top:70px;font-weight:700;font-size:28px;line-height:1}
.welcome h1{left:577px;top:98px;font-family:"Roboto Condensed",sans-serif;font-weight:700;font-size:48px;line-height:1.05;text-transform:uppercase}
.welcome .copy{left:577px;top:168px;width:465px;font-size:11.5px;line-height:1.55}
.welcome .copy p+p{margin-top:12px}

/* menu */
.menu{top:1113px;height:456px;background:#fff;background-image:radial-gradient(#f1f1f1 1px,transparent 1px);background-size:10px 10px}
.menu .script{left:164px;top:18px;font-family:"Great Vibes",cursive;font-size:46px;color:var(--red)}
.menu .script-rule{left:260px;top:48px;width:288px;height:1px;background:#cfcfcf}
.dish{position:absolute;width:200px;text-align:center;transform:translateX(-50%)}
.dish .plate{width:96px;height:96px;margin:0 auto;border-radius:50%;border:2px solid var(--red);padding:5px}
.dish .plate span{display:block;width:100%;height:100%;border-radius:50%;background:radial-gradient(circle at 45% 45%,#8fbf5a,#d8c08a 55%,#7a5a35)}
.dish p{margin-top:12px;font-weight:700;font-size:19px;line-height:1.2;color:#222}
.promo{left:766px;top:2px;width:272px;height:384px;background:var(--card);text-align:center}
.promo .name{position:absolute;left:0;width:272px;top:38px;font-weight:900;font-size:44px;line-height:1.05;color:var(--yellow)}
.promo .photo{left:61px;top:168px;width:150px;height:150px;border-radius:50%;border:4px solid #fff;background:radial-gradient(circle,#d9a34a,#8c4a22 55%,#4c6b2c)}
.promo .call{position:absolute;left:34px;right:0;bottom:0;height:46px;background:var(--yellow);font-family:"Roboto Condensed",sans-serif;font-weight:700;font-size:24px;line-height:46px;color:#1a1a1a}

/* gallery */
.gallery{top:1569px;height:397px;background:linear-gradient(var(--yellow) 0 131px,#3b2d24 131px)}
.gallery h2{left:0;width:1200px;top:40px;text-align:center;font-family:"Roboto Condensed",sans-serif;font-size:34px;color:#1a1a1a}
.gallery .line{top:62px;height:1px;background:#222}
.star{position:absolute;fill:#1a1a1a}
.tile{position:absolute;top:119px;height:219px}
.tile .tab{position:absolute;top:-7px;left:18px;right:18px;height:14px;background:#fff}
.tile .photo{inset:0}
.tile .label{position:absolute;left:18px;right:18px;top:219px;height:45px;background:var(--red);color:#fff;font-weight:700;font-size:19px;text-align:center;line-height:45px}

/* events */
.events{top:1966px;height:342px;background:radial-gradient(ellipse at 20% 40%,#5a3f2d,transparent 60%),radial-gradient(ellipse at 85% 70%,#4a3a26,transparent 55%),#2e241e;color:#fff}
.events h2{left:0;width:1200px;top:30px;text-align:center;font-weight:300;font-size:42px;color:var(--green)}
.event{position:absolute;top:121px;width:290px}
.event .date{position:absolute;left:0;top:0;width:73px;height:75px;border:1.5px solid #ddd;text-align:center}
.event .date b{display:block;font-weight:300;font-size:30px;color:#ffd54a;margin-top:6px}
.event .date span{font-size:14px}
.event .info{position:absolute;left:90px;top:2px;font-size:11px;line-height:1.6}
.event .info .t{color:var(--red)}
.event .info .r{color:#b84a3a;font-size:10px}
.event .more{position:absolute;left:0;top:103px;font-size:11px;color:var(--red)}
.ev-btn{left:493px;top:279px;width:166px;height:34px;background:#e4e4e4;color:#222;border-radius:3px;font-size:12px;font-weight:700;display:flex;align-items:center;justify-content:center;gap:6px}

/* promises */
.promises{top:2308px;height:297px;background:#fff}
.promise{position:absolute;top:64px;width:285px;height:194px;border:1.5px solid var(--red);border-top:none;text-align:center}
.promise .big{position:absolute;left:0;right:0;top:-44px;font-weight:900;font-size:40px;color:var(--green);line-height:1}
.promise h3{position:absolute;left:-10px;right:-10px;top:-6px;font-weight:900;font-size:26px;text-transform:uppercase;color:#111;background:#fff;line-height:1.1}
.promise p{position:absolute;left:20px;right:20px;top:66px;font-size:11px;line-height:1.55}
.promise .rm{position:absolute;left:85px;top:142px;width:116px;height:34px;background:var(--red);color:#fff;font-size:12px;display:flex;align-items:center;justify-content:center;gap:5px}

/* testimonials */
.testimonials{top:2605px;height:456px;background:var(--grey-bg)}
.testimonials h2{left:0;width:1200px;top:74px;text-align:center;font-family:"Roboto Condensed",sans-serif;font-size:34px;color:#1a1a1a}
.avatar{position:absolute;border-radius:50%;border:3px solid #fff}
.t-arrow{position:absolute;top:2821px}
.testimonials .quote{left:360px;width:480px;top:290px;text-align:center;font-size:16px;line-height:1.5;color:#444}
.testimonials .who{left:0;width:1200px;top:380px;text-align:center;font-size:17px;color:#222}
.testimonials .role{left:0;width:1200px;top:404px;text-align:center;font-size:13px;color:var(--red)}

/* footer */
.site-footer{top:3061px;height:361px;background:linear-gradient(90deg,#141414 55%,#2a2420);color:#fff}
.fnav a{position:absolute;top:29px;transform:translateX(-50%);font-size:11px;color:#fff;text-decoration:none}
.fbrand{left:164px;top:80px;font-weight:900;font-size:34px;line-height:1.05;color:var(--yellow)}
.fabout{left:164px;top:174px;width:230px;font-size:11px;line-height:1.5}
.social{position:absolute;top:224px;width:30px;height:30px;border-radius:50%;background:#fff}
.fhead{top:80px;font-size:13px;font-weight:700;text-transform:uppercase}
.map{left:458px;top:100px;width:242px;height:115px;background:linear-gradient(135deg,#e8e8e8,#cfd3d6);border:1px solid #999}
.cline{position:absolute;left:458px;font-size:12px;display:flex;gap:8px;align-items:flex-start}
.cline svg{flex:none;margin-top:1px}
.field{position:absolute;left:775px;width:217px;height:28px;background:#3a3a3a;font-size:11px;color:#aaa;display:flex;align-items:center;gap:8px;padding-left:12px}
.subscribe{left:777px;top:219px;width:94px;height:20px;background:var(--red);font-size:10px;font-weight:700;text-align:center;line-height:20px}
.copyright{left:164px;top:329px;font-size:11px;color:#ccc}
</style>
</head>
<body>

<header class="hero">
  <div class="photo" role="img" aria-label="Photo of a chili skillet topped with cheese, corn muffins and dried corn on a wooden table"></div>
  <div class="abs brand-dot"></div>
  <div class="abs brand">Millbrook Cafe</div>
  <div class="abs rule"></div>
  <div class="arrow" style="left:42px;top:355px"><svg width="12" height="12" viewBox="0 0 12 12"><path d="M8 1 3 6l5 5" fill="none" stroke="#fff" stroke-width="2"/></svg></div>
  <div class="arrow" style="left:1124px;top:355px"><svg width="12" height="12" viewBox="0 0 12 12"><path d="M4 1l5 5-5 5" fill="none" stroke="#fff" stroke-width="2"/></svg></div>
  <div class="btn btn-order"><svg width="22" height="20" viewBox="0 0 22 20"><path d="M1 2h4l3 11h11l2-8H7" fill="none" stroke="#1a1a1a" stroke-width="2.4"/><circle cx="9" cy="17" r="2" fill="#1a1a1a"/><circle cx="18" cy="17" r="2" fill="#1a1a1a"/></svg>Order Now!</div>
  <div class="btn btn-call"><svg width="20" height="20" viewBox="0 0 24 24"><path d="M6.6 10.8a15 15 0 0 0 6.6 6.6l2.2-2.2a1 1 0 0 1 1-.25 11.4 11.4 0 0 0 3.6.6 1 1 0 0 1 1 1V20a1 1 0 0 1-1 1A17 17 0 0 1 3 4a1 1 0 0 1 1-1h3.5a1 1 0 0 1 1 1c0 1.25.2 2.45.6 3.6a1 1 0 0 1-.25 1z" fill="#fff"/></svg>Call Now!</div>
</header>

<div class="topbar abs">
  <span class="mail"><svg width="11" height="8" viewBox="0 0 11 8"><rect width="11" height="8" fill="#fff"/><path d="M0 0l5.5 4L11 0" fill="none" stroke="#e8403a"/></svg>info@millbrookcafe.com</span>
  <span class="phone"><svg width="16" height="16" viewBox="0 0 24 24"><path d="M6.6 10.8a15 15 0 0 0 6.6 6.6l2.2-2.2a1 1 0 0 1 1-.25 11.4 11.4 0 0 0 3.6.6 1 1 0 0 1 1 1V20a1 1 0 0 1-1 1A17 17 0 0 1 3 4a1 1 0 0 1 1-1h3.5a1 1 0 0 1 1 1c0 1.25.2 2.45.6 3.6a1 1 0 0 1-.25 1z" fill="#fff"/></svg>(+1) 313 555 0148</span>
</div>

<nav class="nav abs">
  <a style="left:185px">Home</a><span class="dot" style="left:266px"></span>
  <a style="left:351px">About</a><span class="dot" style="left:433px"></span>
  <a style="left:516px">Menu</a><span class="dot" style="left:598px"></span>
  <a style="left:684px">Feature</a><span class="dot" style="left:768px"></span>
  <a style="left:853px">Shop</a><span class="dot" style="left:937px"></span>
  <a style="left:1024px">Contact</a>
</nav>

<section class="welcome">
  <div class="abs frame"><div class="photo" role="img" aria-label="Collage of salads, burgers and vegetarian plates"></div></div>
  <h2 class="abs">WELCOME TO</h2>
  <h1 class="abs">Millbrook Cafe</h1>
  <div class="abs copy">
    <p>Lorem Ipsum is simply dummy text of the printing and typesetting industry. Lorem Ipsum has been the industry's standard dummy text ever since the 1500s, when an unknown printer took a galley of type and scrambled it to make a type specimen book. It has survived not only five centuries, but also the leap into electronic typesetting, remaining essentially unchanged. It was popularised in the 1960s with the release of Letraset sheets containing Lorem Ipsum passages, and more recently with desktop publishing software like Aldus PageMaker including versions of Lorem Ipsum.</p>
    <p>Lorem Ipsum is simply dummy text of the printing and typesetting industry. Lorem Ipsum has been the industry's standard dummy text ever since the 1500s, when an unknown printer took a galley of type and scrambled it to make a type specimen book. It has survived not only five centuries, but also the leap into electronic typesetting, remaining essentially unchanged.</p>
  </div>
</section>

<section class="menu">
  <div class="abs script">Menu</div>
  <div class="abs script-rule"></div>
  <div class="dish" style="left:230px;top:78px"><div class="plate" role="img" aria-label="Salad dish"><span></span></div><p>Lorem Ipsum is<br>simply dummy</p></div>
  <div class="dish" style="left:443px;top:78px"><div class="plate" role="img" aria-label="Pasta dish"><span></span></div><p>Lorem Ipsum is<br>simply dummy</p></div>
  <div class="dish" style="left:655px;top:78px"><div class="plate" role="img" aria-label="Vegetable plate"><span></span></div><p>Lorem Ipsum is<br>simply dummy</p></div>
  <div class="dish" style="left:230px;top:242px"><div class="plate" role="img" aria-label="Salad dish"><span></span></div><p>Lorem Ipsum is<br>simply dummy</p></div>
  <div class="dish" style="left:443px;top:242px"><div class="plate" role="img" aria-label="Pasta dish"><span></span></div><p>Lorem Ipsum is<br>simply dummy</p></div>
  <div class="dish" style="left:655px;top:242px"><div class="plate" role="img" aria-label="Vegetable plate"><span></span></div><p>Lorem Ipsum is<br>simply dummy</p></div>
  <div class="abs promo">
    <div class="name">Millbrook<br>Cafe</div>
    <div class="photo" role="img" aria-label="Veggie sandwich"></div>
    <div class="call">(+1) 313 555 0148</div>
  </div>
</section>

<section class="gallery">
  <div class="abs line" style="left:238px;width:200px"></div>
  <div class="abs line" style="left:764px;width:192px"></div>
  <svg class="star" style="left:378px;top:66px" width="14" height="14" viewBox="0 0 10 10"><path d="M5 0l1.2 3.6H10L7 5.8 8.1 9.5 5 7.2 1.9 9.5 3 5.8 0 3.6h3.8z"/></svg>
  <svg class="star" style="left:398px;top:56px" width="14" height="14" viewBox="0 0 10 10"><path d="M5 0l1.2 3.6H10L7 5.8 8.1 9.5 5 7.2 1.9 9.5 3 5.8 0 3.6h3.8z"/></svg>
  <svg class="star" style="left:416px;top:66px" width="12" height="12" viewBox="0 0 10 10"><path d="M5 0l1.2 3.6H10L7 5.8 8.1 9.5 5 7.2 1.9 9.5 3 5.8 0 3.6h3.8z"/></svg>
  <svg class="star" style="left:752px;top:44px" width="14" height="14" viewBox="0 0 10 10"><path d="M5 0l1.2 3.6H10L7 5.8 8.1 9.5 5 7.2 1.9 9.5 3 5.8 0 3.6h3.8z"/></svg>
  <svg class="star" style="left:772px;top:32px" width="14" height="14" viewBox="0 0 10 10"><path d="M5 0l1.2 3.6H10L7 5.8 8.1 9.5 5 7.2 1.9 9.5 3 5.8 0 3.6h3.8z"/></svg>
  <svg class="star" style="left:792px;top:22px" width="14" height="14" viewBox="0 0 10 10"><path d="M5 0l1.2 3.6H10L7 5.8 8.1 9.5 5 7.2 1.9 9.5 3 5.8 0 3.6h3.8z"/></svg>
  <h2 class="abs">FOOD GALLERY</h2>
  <div class="tile" style="left:0;width:299px"><div class="tab"></div><div class="photo" role="img" aria-label="Falafel pita sandwiches" style="background:linear-gradient(135deg,#d9c8a8,#b36a35 50%,#6c8a3a)"></div><div class="label">Vegetarian Food - 1</div></div>
  <div class="tile" style="left:299px;width:299px"><div class="tab"></div><div class="photo" role="img" aria-label="Bowl of fresh salad" style="background:linear-gradient(135deg,#e5e2dc,#b8503a 45%,#7fa04a)"></div><div class="label">Vegetarian Food - 2</div></div>
  <div class="tile" style="left:598px;width:299px"><div class="tab"></div><div class="photo" role="img" aria-label="Bowls of chopped vegetables" style="background:linear-gradient(135deg,#4c7a2c,#9fbf5a 45%,#c0392b 75%,#3d3a32)"></div><div class="label">Vegetarian Food - 3</div></div>
  <div class="tile" style="left:897px;width:303px"><div class="tab"></div><div class="photo" role="img" aria-label="Veggie burgers with onion" style="background:linear-gradient(135deg,#7a4a2a,#c97b4a 45%,#9a3a5a 75%,#e6d9c0)"></div><div class="label">Vegetarian Food - 4</div></div>
  <div class="arrow" style="left:18px;top:212px;border-color:#fff;background:rgba(0,0,0,.35)"><svg width="12" height="12" viewBox="0 0 12 12"><path d="M8 1 3 6l5 5" fill="none" stroke="#fff" stroke-width="2"/></svg></div>
  <div class="arrow" style="left:1148px;top:212px;border-color:#fff;background:rgba(0,0,0,.35)"><svg width="12" height="12" viewBox="0 0 12 12"><path d="M4 1l5 5-5 5" fill="none" stroke="#fff" stroke-width="2"/></svg></div>
</section>

<section class="events">
  <h2 class="abs">Upcoming Events</h2>
  <div class="event" style="left:164px">
    <div class="date"><b>01</b><span>July</span></div>
    <div class="info"><div class="t">Lorem Ipsum simply dummy text</div><div>&#9719; 07/1/2015 | 8:30 pm - 11:00 pm</div><div class="r">Recurring Event (See all)</div><div>&#9679; Lakeview Hall</div></div>
    <div class="more">View More....</div>
  </div>
  <div class="event" style="left:468px">
    <div class="date"><b>01</b><span>July</span></div>
    <div class="info"><div class="t">Lorem Ipsum simply dummy text</div><div>&#9719; 07/1/2015 | 8:30 pm - 11:00 pm</div><div class="r">Recurring Event (See all)</div><div>&#9679; Lakeview Hall</div></div>
    <div class="more">View More....</div>
  </div>
  <div class="event" style="left:773px">
    <div class="date"><b>01</b><span>July</span></div>
    <div class="info"><div class="t">Lorem Ipsum simply dummy text</div><div>&#9719; 07/1/2015 | 8:30 pm - 11:00 pm</div><div class="r">Recurring Event (See all)</div><div>&#9679; Lakeview Hall</div></div>
    <div class="more">View More....</div>
  </div>
  <div class="abs ev-btn">ENTER NEW EVENTS <svg width="13" height="13" viewBox="0 0 14 14"><circle cx="7" cy="7" r="6" fill="none" stroke="#222" stroke-width="1.6"/><path d="M6 4l3 3-3 3" fill="none" stroke="#222" stroke-width="1.6"/></svg></div>
</section>

<section class="promises">
  <div class="promise" style="left:144px"><div class="big">100%</div><h3>Scratch Kitchen</h3><p>Lorem Ipsum is simply dummy text of the printing and typesetting industry. Lorem Ipsum has been the industry's standard dummy text ever since the...</p><div class="rm">&#9679; Read More...</div></div>
  <div class="promise" style="left:456px"><div class="big">100%</div><h3>Certified Organic</h3><p>Lorem Ipsum is simply dummy text of the printing and typesetting industry. Lorem Ipsum has been the industry's standard dummy text ever since the...</p><div class="rm">&#9679; Read More...</div></div>
  <div class="promise" style="left:769px"><div class="big">STRICT</div><h3>Sustainable Plan</h3><p>Lorem Ipsum is simply dummy text of the printing and typesetting industry. Lorem Ipsum has been the industry's standard dummy text ever since the...</p><div class="rm">&#9679; Read More...</div></div>
</section>

<section class="testimonials">
  <svg class="abs" style="left:408px;top:80px" width="40" height="40" viewBox="0 0 40 40"><path fill="#e8403a" d="M10 16l2 5h5l-4 3 1.5 5-4.5-3-4.5 3L7 24l-4-3h5z"/></svg>
  <svg class="abs" style="left:752px;top:50px" width="70" height="40" viewBox="0 0 70 40"><path fill="#e8403a" d="M10 20l2 5h5l-4 3 1.5 5-4.5-3-4.5 3L7 28l-4-3h5zM36 10l2 5h5l-4 3 1.5 5-4.5-3-4.5 3L33 18l-4-3h5zM60 0l2 5h5l-4 3 1.5 5-4.5-3-4.5 3L57 8l-4-3h5z"/></svg>
  <h2 class="abs">TESTIMONIALS</h2>
  <div class="avatar" role="img" aria-label="Client portrait" style="left:474px;top:177px;width:78px;height:78px;background:#8da6b8"></div>
  <div class="avatar" role="img" aria-label="Client portrait" style="left:559px;top:168px;width:96px;height:96px;background:#6d6d6d"></div>
  <div class="avatar" role="img" aria-label="Client portrait" style="left:664px;top:177px;width:78px;height:78px;background:#d8d2cc"></div>
  <div class="arrow" style="left:161px;top:199px;border-color:var(--red);width:32px;height:32px"><svg width="12" height="12" viewBox="0 0 12 12"><path d="M11 6H2m4-4L2 6l4 4" fill="none" stroke="#e8403a" stroke-width="1.6"/></svg></div>
  <div class="arrow" style="left:1006px;top:199px;border-color:var(--red);width:32px;height:32px"><svg width="12" height="12" viewBox="0 0 12 12"><path d="M1 6h9M6 2l4 4-4 4" fill="none" stroke="#e8403a" stroke-width="1.6"/></svg></div>
  <div class="abs quote">&ldquo; Lorem Ipsum is simply dummy text of the printing and typesetting industry. Lorem Ipsum has been the industry's standard dummy text ever since the 1500s. &rdquo;</div>
  <div class="abs who">Dana Reyes</div>
  <div class="abs role">Happy client</div>
</section>

<footer class="site-footer">
  <div class="fnav">
    <a style="left:294px">HOME</a><a style="left:410px">ABOUT US</a><a style="left:531px">MENU</a><a style="left:666px">FEATURES</a><a style="left:778px">SHOP</a><a style="left:894px">CONTACT</a>
  </div>
  <div class="abs fbrand">Millbrook<br>Cafe</div>
  <div class="abs fabout">Lorem Ipsum is simply dummy text of the printing and but release of Letraset sheets containing</div>
  <span class="social" style="left:160px"></span><span class="social" style="left:198px"></span><span class="social" style="left:236px"></span><span class="social" style="left:274px"></span><span class="social" style="left:312px"></span>
  <div class="abs fhead" style="left:458px">Contact Information</div>
  <div class="abs map" role="img" aria-label="Location map"></div>
  <div class="cline" style="top:226px;font-weight:500"><svg width="10" height="14" viewBox="0 0 10 14"><path d="M5 0a5 5 0 0 0-5 5c0 4 5 9 5 9s5-5 5-9a5 5 0 0 0-5-5z" fill="#fbd92b"/><circle cx="5" cy="5" r="1.8" fill="#141414"/></svg><span>Lorem Ipsum is simply dummy text of<br>the printing and typesetting industry.</span></div>
  <div class="cline" style="top:267px"><svg width="12" height="12" viewBox="0 0 24 24"><path d="M6.6 10.8a15 15 0 0 0 6.6 6.6l2.2-2.2a1 1 0 0 1 1-.25 11.4 11.4 0 0 0 3.6.6 1 1 0 0 1 1 1V20a1 1 0 0 1-1 1A17 17 0 0 1 3 4a1 1 0 0 1 1-1h3.5a1 1 0 0 1 1 1c0 1.25.2 2.45.6 3.6a1 1 0 0 1-.25 1z" fill="#fbd92b"/></svg><span>(+1) 313 555 0148</span></div>
  <div class="cline" style="top:294px"><svg width="12" height="9" viewBox="0 0 11 8"><rect width="11" height="8" fill="#fbd92b"/><path d="M0 0l5.5 4L11 0" fill="none" stroke="#141414"/></svg><span>info@millbrookcafe.com</span></div>
  <div class="abs fhead" style="left:775px">Subscribe Newsletter:</div>
  <div class="field" style="top:125px">&#9679; Name</div>
  <div class="field" style="top:166px">&#9993; Email Id</div>
  <div class="abs subscribe">SUBSCRIBE</div>
  <div class="abs copyright">&copy; 2017 Millbrook Cafe. All rights reserved.</div>
</footer>

</body>
</html>
```